NimbusFern cyber security firm Website

We did our website ourselves on Joomla, it's not great. We want a wordpress based redesign. Some thing that will represent a modern cyber security firm that's aimed at solving business problems.
Https://nimbusfern.co.nz (current site)
#58427c - primary color (you'll know why when you see it's name)
Logo files can be provided. Ask for more info if you need.

We want a modern, quick to load website. Website is going to have a home - services - products - about us - blogs menu. Will need a footer menu, site map, contact page etc.
We getting Content done sperately.
Our logo is #58427c - so hoping for a light theme (or at least the top is).
While we have been specific around the color - we are not after a website that has too much of it.

Reference sites that we like :
https://www.voltaline.co.nz/ - Love the full screen real world image
https://wardvex.co.nz/ (love the real world imagry and motion)
https://www.qtr.com/us-en?lnk=m
https://redowlen.com

Please dont use :
cartoon or redered images : (Like this : https://img.stockmorra.com/free-vector/cyber-security-concept_23-2148543851.jpg?w=2000 )

Please don't use images like this : https://www.tavelundi.com/eu/blog/oil-gas/app/uploads/2020/04/116137226_s-1440x564_c.jpg - they are old and boring.

We would like to see some creativity - loading our logo into a readymade wordpress template and hitting go won't cut it.
Updates

Thanks everyone who has submitted so far. We've extended the deadline as we wanted to give everyone a chance to Re- read the brief and perhaps make some tweeks should they feel it necessary.

Target Market(s)

Mid - large enterprise, finance, insurance, utilities vertical

Industry/Entity Type

Cyber security

Coding

Coded - Design and coding required

Number of Pages Required

5+ page

Font styles to use
Other font styles liked:
• Open sans

Colors

Designer to choose colors to be used in the design.

Requirements
Must have
• Simple clear messaging, something that catches user engagement
Nice to have
• Motion of some sort, but not overdone, GDPR

```html
<!DOCTYPE html>
<html lang="en">
<head>
<meta charset="utf-8">
<title>NimbusFern — Third-party Risk Management</title>
<link href="https://fonts.googleapis.com/css2?family=Montserrat:wght@400;500;600;700&family=Open+Sans:wght@400;600&display=swap" rel="stylesheet">
<style>
:root{
  --primary:#58427c;
  --primary-deep:#3f2d5c;
  --primary-soft:#d6cde3;
  --primary-tint:#ece6f4;
  --ink:#222;
  --muted:#4a4a4a;
  --band:#f6f6f7;
  --white:#fff;
}
*{margin:0;padding:0;box-sizing:border-box}
html,body{width:1200px;height:3575px;overflow:hidden}
body{position:relative;background:var(--white);font-family:"Open Sans",sans-serif;color:var(--ink)}
.abs{position:absolute}
.heading{font-family:"Montserrat",sans-serif;color:var(--primary);font-weight:400;line-height:1.25}
.heading b{font-weight:700}
.copy{font-size:12.5px;line-height:21px;color:var(--muted)}
.pill{position:absolute;display:flex;align-items:center;justify-content:space-between;border-radius:20px;padding:0 4px 0 18px;font-family:"Montserrat",sans-serif;font-size:12.5px;text-transform:uppercase}
.pill .dot{width:30px;height:30px;border-radius:50%;background:var(--white);border:2px solid var(--primary)}
.pill--dark{background:var(--primary);color:var(--white)}
.pill--light{background:var(--white);color:var(--primary)}
.brand{display:flex;align-items:center;gap:10px;font-family:"Montserrat",sans-serif;font-weight:600;color:var(--primary);letter-spacing:1px}
.brand .mark{width:30px;height:30px;border-radius:50%;background:var(--primary)}
.nav-item{position:absolute;top:31px;font-family:"Montserrat",sans-serif;font-size:12.5px;color:var(--ink)}
.nav-item--active{color:var(--primary)}
.emblem{position:absolute;display:flex;flex-direction:column;align-items:center;justify-content:center;gap:26px}
.emblem .disc{border-radius:50%}
.emblem .name{font-family:"Montserrat",sans-serif;font-weight:600;letter-spacing:2px}
.feature-circle{position:absolute;top:1283px;width:232px;height:232px;border-radius:50%;background:linear-gradient(150deg,#6d5890 0%,#4e3a6f 55%,#3a2a54 100%);display:flex;align-items:center;justify-content:center;color:var(--white)}
.feature-circle svg{width:72px;height:72px}
.feature-line{position:absolute;top:1400px;width:2px;height:143px;background:#ccc}
.feature-dot{position:absolute;top:1537px;width:11px;height:11px;border-radius:50%;background:var(--primary)}
.feature-text{position:absolute;top:1528px;width:165px;font-family:"Montserrat",sans-serif;font-size:17px;line-height:26.5px;color:var(--ink)}
.service-card{position:absolute;width:194px;height:172px;border-radius:4px;background:var(--primary-soft);display:flex;flex-direction:column;align-items:center;justify-content:center;gap:12px;text-align:center;font-family:"Montserrat",sans-serif;font-size:16.5px;line-height:24px;color:var(--primary)}
.service-card--active{background:var(--primary);color:var(--white)}
.service-card svg{width:40px;height:40px}
.partner{position:absolute;top:2462px;width:252px;height:172px;background:var(--white);box-shadow:0 2px 10px rgba(0,0,0,.08);display:flex;align-items:center;justify-content:center;font-family:"Montserrat",sans-serif;font-weight:700;font-size:26px}
.footer-title{font-family:"Montserrat",sans-serif;font-size:16px;font-weight:500;color:var(--primary)}
.footer-title::after{content:"";display:block;width:52px;height:2px;background:var(--primary);margin-top:6px;opacity:.5}
.footer-links{list-style:none;font-size:12.5px;color:var(--muted);text-transform:uppercase}
.footer-links li{height:34.5px}
.contact-row{display:flex;align-items:center;gap:16px;font-size:12.5px;color:var(--muted);height:37px}
.social{position:absolute;top:3433px;width:30px;height:30px;border-radius:50%;border:1.5px solid var(--primary)}
</style>
</head>
<body>

<header>
  <div class="abs brand" style="left:60px;top:22px;font-size:25px"><span class="mark"></span>NIMBUSFERN</div>
  <span class="nav-item nav-item--active" style="left:540px">HOME</span>
  <span class="nav-item" style="left:618px">SERVICES</span>
  <span class="nav-item" style="left:716px">PRODUCTS</span>
  <span class="nav-item" style="left:821px">BLOGS</span>
  <span class="nav-item" style="left:900px">CONTACT US</span>
  <div class="pill pill--dark" style="left:1012px;top:20px;width:128px;height:38px">Free Scan<span class="dot"></span></div>
</header>

<section class="hero">
  <h1 class="abs heading" style="left:62px;top:198px;font-size:56px;line-height:66px"><b>Third-party</b> Risk<br>Management</h1>
  <p class="abs copy" style="left:62px;top:341px;width:440px">We provide the full detail, providing a multidimensional view of your entire attack surface from a technical, financial impact and a compliance perspective.</p>
  <div class="pill pill--dark" style="left:60px;top:443px;width:168px;height:38px">Demo Platform<span class="dot"></span></div>
  <div class="emblem" style="left:660px;top:110px;width:480px;height:480px">
    <span class="disc" style="width:330px;height:330px;background:var(--primary)"></span>
    <span class="name" style="font-size:34px;color:var(--primary)">NIMBUSFERN</span>
  </div>
</section>

<svg class="abs" style="left:0;top:630px" width="1200" height="610" aria-hidden="true"><polygon points="0,7 1200,90 1200,602 0,520" fill="var(--band)"/></svg>
<section class="about">
  <h2 class="abs heading" style="left:542px;top:790px;font-size:30.5px;line-height:45px"><b>The tech you use to run your business</b><br>could be used to sabotage it!</h2>
  <div class="abs copy" style="left:542px;top:890px;width:600px;font-size:12px">
    <p style="margin-bottom:14px">In the course of doing business, your company could deal with dozens of third-party vendors: suppliers, manufacturers, service providers, affiliate offices, distributors, resellers, agents, contractors, the list goes on … all of whom, in turn, deal with dozens of their own vendors. It's easy to see then why third-party cyber risk management is becoming such a high priority for businesses that deal with confidential data. (Lawyers, accountants, insurers, to name just three.)</p>
    <p style="margin-bottom:14px">NimbusFern is a 100% New Zealand owned and operated cyber security company, designed to protect your business against exactly this kind of risk by offering third-party risk management and cyber security solutions.</p>
    <p>In short, offering small and medium sized businesses the same standard of cyber security as a large organisations – at a price that makes sense.</p>
  </div>
</section>

<section class="features">
  <div class="feature-line" style="left:64px"></div><div class="feature-line" style="left:283px"></div><div class="feature-line" style="left:494px"></div><div class="feature-line" style="left:705px"></div><div class="feature-line" style="left:915px"></div>

  <div class="feature-circle" style="left:64px" role="img" aria-label="Photo of a laptop and bar chart with purple overlay, warning icon">
    <svg viewBox="0 0 64 64" fill="none" stroke="currentColor" stroke-width="3" stroke-linejoin="round" stroke-linecap="round"><path d="M32 6 50 38H14z"/><path d="M32 18v10M32 33v1"/><path d="M8 46h12l8 4h12a3 3 0 0 1 0 6H26M40 52l14-8a3 3 0 0 1 4 4L42 60H8"/></svg>
  </div>
  <div class="feature-circle" style="left:275px" role="img" aria-label="Photo of a business person holding a tablet with purple overlay, gears icon">
    <svg viewBox="0 0 64 64" fill="none" stroke="currentColor" stroke-width="3" stroke-linecap="round"><circle cx="32" cy="14" r="6"/><circle cx="32" cy="32" r="6"/><circle cx="32" cy="50" r="6"/><path d="M14 54V20M9 25l5-5 5 5M50 54V20M45 25l5-5 5 5"/></svg>
  </div>
  <div class="feature-circle" style="left:486px" role="img" aria-label="Photo of a hooded masked figure with purple overlay, calculator icon">
    <svg viewBox="0 0 64 64" fill="none" stroke="currentColor" stroke-width="3" stroke-linejoin="round"><rect x="6" y="6" width="24" height="34" rx="2"/><path d="M11 12h14v6H11zM11 24h4M18 24h4M11 30h4M18 30h4"/><path d="M34 10h20v26M38 18h12M38 24h12M38 30h6"/><circle cx="28" cy="46" r="10"/><path d="M31 42h-4a2 2 0 0 0 0 4h2a2 2 0 0 1 0 4h-4M28 40v2M28 50v2M46 58l12-16"/></svg>
  </div>
  <div class="feature-circle" style="left:697px" role="img" aria-label="Photo of market data screens with purple overlay, globe monitor icon">
    <svg viewBox="0 0 64 64" fill="none" stroke="currentColor" stroke-width="3" stroke-linejoin="round"><rect x="8" y="26" width="48" height="26" rx="2"/><path d="M26 58h12M32 52v6"/><circle cx="32" cy="24" r="14" fill="#4e3a6f"/><path d="M18 24h28M32 10c-6 8-6 20 0 28M32 10c6 8 6 20 0 28"/><path d="M50 8l4-4M54 10h4"/></svg>
  </div>
  <div class="feature-circle" style="left:908px" role="img" aria-label="Photo of letter blocks on a keyboard with purple overlay, rising bars icon">
    <svg viewBox="0 0 64 64" fill="none" stroke="currentColor" stroke-width="3" stroke-linejoin="round" stroke-linecap="round"><rect x="8" y="40" width="12" height="18"/><rect x="26" y="30" width="12" height="28"/><rect x="44" y="36" width="12" height="22"/><path d="M14 34V20M10 24l4-4 4 4M50 30V8M46 12l4-4 4 4"/><circle cx="32" cy="16" r="8"/><path d="M34 13h-3a1.5 1.5 0 0 0 0 3h2a1.5 1.5 0 0 1 0 3h-3"/></svg>
  </div>

  <div class="feature-dot" style="left:59px"></div><div class="feature-dot" style="left:278px"></div><div class="feature-dot" style="left:489px"></div><div class="feature-dot" style="left:700px"></div><div class="feature-dot" style="left:910px"></div>
  <p class="feature-text" style="left:93px;width:165px">Reduce your Third-party risk management from weeks to hours</p>
  <p class="feature-text" style="left:309px;width:165px">get the full vendor risk view across your whole supply chain</p>
  <p class="feature-text" style="left:518px;width:165px">Calculate, continuously monitor and reduce your cyber security risk.</p>
  <p class="feature-text" style="left:735px;width:165px">Save time and resources in cyber risk assessments</p>
  <p class="feature-text" style="left:945px;width:120px">Extremely competitive pricing.</p>
</section>

<svg class="abs" style="left:0;top:1708px" width="1200" height="642" aria-hidden="true"><polygon points="0,88 1200,0 1200,582 0,640" fill="var(--band)"/></svg>
<section class="services">
  <h2 class="abs heading" style="left:62px;top:1882px;font-size:32px"><b>Our</b> Services</h2>
  <p class="abs copy" style="left:62px;top:1932px;width:370px;font-size:12px">Lorem Ipsum is simply dummy text of the printing and typesetting industry. Lorem Ipsum has been the industry's standard dummy text ever since the 1500s, when an unknown printer took a galley of type and scrambled it to make a type specimen book.</p>
  <div class="pill pill--dark" style="left:60px;top:2074px;width:134px;height:38px">View More<span class="dot"></span></div>

  <div class="service-card" style="left:522px;top:1917px">
    <svg viewBox="0 0 40 40" fill="none" stroke="currentColor" stroke-width="2" stroke-linejoin="round" stroke-linecap="round"><path d="M8 4h18l6 6v24H8z"/><path d="M13 12h10M13 17h12M13 22h6"/><circle cx="26" cy="27" r="5"/><path d="M30 31l6 6"/></svg>
    Security<br>assessments</div>
  <div class="service-card service-card--active" style="left:735px;top:1798px">
    <svg viewBox="0 0 40 40" fill="none" stroke="currentColor" stroke-width="2" stroke-linejoin="round" stroke-linecap="round"><rect x="4" y="5" width="32" height="22" rx="2"/><path d="M14 34h12M20 27v7"/><circle cx="13" cy="12" r="2.5"/><circle cx="27" cy="12" r="2.5"/><path d="M9 22a4 4 0 0 1 8 0M23 22a4 4 0 0 1 8 0"/></svg>
    Virtual CISO</div>
  <div class="service-card" style="left:735px;top:1995px">
    <svg viewBox="0 0 40 40" fill="none" stroke="currentColor" stroke-width="2" stroke-linejoin="round" stroke-linecap="round"><path d="M20 3 34 8v10c0 9-6 15-14 19C12 33 6 27 6 18V8z"/><rect x="14" y="18" width="12" height="9" rx="1"/><path d="M16 18v-3a4 4 0 0 1 8 0v3"/></svg>
    Cyber Security<br>assessments</div>
  <div class="service-card" style="left:946px;top:1845px">
    <svg viewBox="0 0 40 40" fill="none" stroke="currentColor" stroke-width="2" stroke-linejoin="round" stroke-linecap="round"><circle cx="12" cy="14" r="4"/><path d="M5 34V26a7 7 0 0 1 14 0v8"/><circle cx="28" cy="13" r="8"/><circle cx="28" cy="13" r="3"/><path d="M22 34h14M26 34V26M32 34V24"/></svg>
    Human Risk<br>Management</div>
  <div class="service-card" style="left:946px;top:2043px">
    <svg viewBox="0 0 40 40" fill="none" stroke="currentColor" stroke-width="2" stroke-linejoin="round" stroke-linecap="round"><path d="M20 3 34 8v10c0 9-6 15-14 19C12 33 6 27 6 18V8z"/><path d="M14 19l4 4 8-8"/></svg>
    Cyber Security<br>Warrant of<br>Fitness</div>
</section>

<section class="partners">
  <h2 class="abs heading" style="left:0;width:1200px;top:2396px;font-size:32px;text-align:center"><b>Our Trusted</b> Partners</h2>
  <div class="partner" style="left:60px"><span role="img" aria-label="Locally owned badge" style="width:112px;height:112px;border-radius:50%;background:#8a8a8a"></span></div>
  <div class="partner" style="left:338px;color:#1a73c8">Altocirra</div>
  <div class="partner" style="left:614px;color:#1a9ad6">Lumora</div>
  <div class="partner" style="left:888px;color:#111">Redowlen</div>
</section>

<svg class="abs" style="left:0;top:2710px" width="1200" height="565" aria-hidden="true"><polygon points="0,0 1200,85 1200,565 0,480" fill="var(--primary)"/></svg>
<section class="cta">
  <h2 class="abs heading" style="left:62px;top:2840px;font-size:32px;line-height:45px;color:var(--white)"><b>We Help You To Have</b> Cyber<br>Security NimbusFern</h2>
  <p class="abs copy" style="left:62px;top:2945px;width:540px;font-size:12px;color:var(--white)">Lorem Ipsum is simply dummy text of the printing and typesetting industry. Lorem Ipsum has been the industry's standard dummy text ever since the 1500s, when an unknown printer</p>
  <div class="pill pill--light" style="left:60px;top:3048px;width:174px;height:38px">Request a Demo<span class="dot"></span></div>
  <div class="emblem" style="left:740px;top:2830px;width:410px;height:380px;gap:22px">
    <span class="disc" style="width:260px;height:260px;background:var(--white)"></span>
    <span class="name" style="font-size:28px;color:var(--white)">NIMBUSFERN</span>
  </div>
</section>

<footer>
  <div class="abs" style="left:60px;top:3300px;width:252px;display:flex;flex-direction:column;align-items:center;gap:12px">
    <span style="width:52px;height:52px;border-radius:50%;background:var(--primary)"></span>
    <span class="brand" style="font-size:30px">NIMBUSFERN</span>
  </div>
  <span class="social" style="left:62px"></span><span class="social" style="left:102px"></span><span class="social" style="left:142px"></span><span class="social" style="left:187px"></span>

  <div class="abs" style="left:338px;top:3297px">
    <h3 class="footer-title">Site Map</h3>
    <ul class="footer-links" style="margin-top:22px">
      <li>Home</li><li>Services</li><li>Products</li><li>Blogs</li><li>Contact Us</li>
    </ul>
  </div>

  <div class="abs" style="left:615px;top:3297px">
    <h3 class="footer-title">Contact Us</h3>
    <div style="margin-top:14px">
      <div class="contact-row"><svg width="18" height="18" viewBox="0 0 18 18"><path d="M3 10a6 6 0 0 1 12 0v3h-3v-4h2M3 13v-4h3v4z" fill="none" stroke="var(--primary)" stroke-width="1.8"/></svg>+64(0)2104417320</div>
      <div class="contact-row"><svg width="18" height="14" viewBox="0 0 18 14"><rect x="1" y="1" width="16" height="12" fill="var(--primary)"/><path d="M1 1l8 7 8-7" fill="none" stroke="#fff" stroke-width="1.4"/></svg>info@nimbusfern.co.nz</div>
      <div class="contact-row"><svg width="18" height="18" viewBox="0 0 18 18"><circle cx="9" cy="9" r="8" fill="var(--primary)"/><path d="M9 4v5h4" fill="none" stroke="#fff" stroke-width="1.6"/></svg>Mon - Fri 8am - 5pm</div>
    </div>
  </div>

  <div class="abs" style="left:889px;top:3297px;width:251px">
    <h3 class="footer-title">Subscribe To Our Newslatter</h3>
    <div style="margin-top:20px;height:38px;border:1.5px solid var(--primary);border-radius:20px;padding:0 18px;display:flex;align-items:center;font-size:12px">E-MAIL</div>
    <div style="margin-top:17px;width:107px;height:34px;border-radius:18px;background:var(--primary);color:var(--white);display:flex;align-items:center;justify-content:center;font-family:'Montserrat',sans-serif;font-size:12px">SUBSCRIBE</div>
  </div>

  <div class="abs" style="left:0;top:3536px;width:1200px;height:1px;background:#ccc"></div>
  <p class="abs" style="left:0;top:3548px;width:1200px;text-align:center;font-size:12px;color:var(--muted)">© 2022 NimbusFern Ltd. All Rights Reserved.</p>
</footer>

</body>
</html>
```